Banner Design Project

I need a banner designed that will be used in an outdoor location. The banner is 8' x 3' and can be full color.

This is a general advertising banner for a photography business; I can provide images if needed;

My website is: www.darvomkellphotography.com

It will be used at the following school: http://www.qbtrm.com/

Target Market(s)

All ages but should appeal to High School Students

Industry/Entity Type

Advertising

Requirements
Must have
• Integrate Logo

```html
<!DOCTYPE html>
<html lang="en">
<head>
<meta charset="utf-8">
<title>Darvom Kell Photography Banner</title>
<link rel="stylesheet" href="https://fonts.googleapis.com/css2?family=Questrial&family=Roboto:wght@300&display=swap">
<style>
  :root {
    --deep-teal: #0f3a3f;
    --moss: #55783a;
    --amber: #a0712c;
    --umber: #4a2e14;
    --lens-dark: #141418;
    --lens-violet: #5b3a9c;
    --url-grey: #e6e6e6;
    --name-white: #ffffff;
    --photo-border: #f2f2f2;
  }
  * { margin: 0; padding: 0; box-sizing: border-box; }
  html, body { width: 1200px; height: 450px; overflow: hidden; background: #222; }
  .banner {
    position: relative;
    width: 1200px;
    height: 450px;
    overflow: hidden;
    background:
      radial-gradient(ellipse 220px 180px at 420px 300px, rgba(235,245,200,0.85), rgba(235,245,200,0) 70%),
      radial-gradient(ellipse 260px 200px at 330px 120px, rgba(160,190,110,0.7), rgba(160,190,110,0) 70%),
      radial-gradient(ellipse 300px 240px at 640px 90px, rgba(190,150,70,0.7), rgba(190,150,70,0) 70%),
      radial-gradient(ellipse 320px 260px at 1100px 300px, rgba(200,130,50,0.75), rgba(200,130,50,0) 70%),
      radial-gradient(ellipse 260px 200px at 200px 420px, rgba(20,70,80,0.9), rgba(20,70,80,0) 70%),
      linear-gradient(90deg, var(--deep-teal) 0%, var(--moss) 30%, #8f8a4a 55%, var(--amber) 75%, var(--umber) 100%);
  }
  .lens-art {
    position: absolute;
    left: -175px;
    top: 25px;
    width: 360px;
    height: 360px;
    border-radius: 50%;
    background:
      radial-gradient(circle at 60% 50%, var(--lens-violet) 0%, #2a2050 45%, var(--lens-dark) 62%, #3a3a40 70%, var(--lens-dark) 78%);
  }
  .site-url {
    position: absolute;
    left: 525px;
    top: 40px;
    font-family: "Roboto", Arial, sans-serif;
    font-weight: 300;
    font-size: 22px;
    color: var(--url-grey);
  }
  .brand {
    position: absolute;
    left: 196px;
    top: 210px;
    width: 484px;
    font-family: "Questrial", "Century Gothic", sans-serif;
    font-weight: 400;
    color: var(--name-white);
  }
  .brand-name {
    display: block;
    font-size: 42px;
    line-height: 52px;
    letter-spacing: 18px;
    padding-left: 6px;
    white-space: nowrap;
  }
  .brand-line {
    display: block;
    font-size: 15px;
    line-height: 20px;
    letter-spacing: 7.5px;
    text-align: right;
    margin-top: 6px;
    margin-right: -6px;
    white-space: nowrap;
  }
  .photo {
    position: absolute;
    box-shadow: 0 4px 10px rgba(0,0,0,0.35);
  }
  .photo-surf {
    left: 682px; top: 88px; width: 225px; height: 125px;
    background: linear-gradient(160deg, #3f8fc4 0%, #2f8c86 45%, #1d5a48 100%);
  }
  .photo-sunset {
    left: 765px; top: 182px; width: 200px; height: 146px;
    background: linear-gradient(180deg, #3c3b40 0%, #a4896a 38%, #6d5e52 55%, #2a2829 100%);
  }
  .photo-singer {
    left: 906px; top: -2px; width: 265px; height: 184px;
    background: linear-gradient(120deg, #5a3320 0%, #c8896a 45%, #a55b3a 70%, #3a2418 100%);
  }
  .photo-portrait {
    left: 964px; top: 151px; width: 175px; height: 260px;
    border: 2px solid var(--photo-border);
    background: linear-gradient(180deg, #e9eae8 0%, #dcdedb 100%);
  }
</style>
</head>
<body>
  <div class="banner">
    <div class="lens-art" role="img" aria-label="Close-up of a camera lens with violet glass"></div>

    <p class="site-url">www.darvomkellphotography.com</p>

    <div class="brand">
      <span class="brand-name">DARVOM KELL</span>
      <span class="brand-line">PHOTOGRAPHY</span>
    </div>

    <div class="photo photo-surf" role="img" aria-label="Photo of a bodyboarder riding a breaking wave"></div>
    <div class="photo photo-singer" role="img" aria-label="Photo of a singer with windswept hair at a microphone"></div>
    <div class="photo photo-sunset" role="img" aria-label="Photo of a parent lifting a child in silhouette at sunset on the beach"></div>
    <div class="photo photo-portrait" role="img" aria-label="Studio portrait of a woman holding a glass, standing on a white backdrop"></div>
  </div>
</body>
</html>
```